RP-Steuerberatung WordPress Site fully implemented (tax advisor)

Hello!
I need a little Wordpress Site for my newly founded Tax-Advisor Company.
I am a one-man Office advising in the area of Crypto-Currency.
PLEASE only provide a Design, if you can also Implement a WP-Site afterwards on an existing Webspace.

Please find the Content and Website-Description in the attached Document

Language for the Website is German (for now)

Target Market(s)

Tax-Advisory (specialized in Crypto Currency)

Coding

Coded - Design and coding required

Number of Pages Required

5+ page

Font styles to use
Sans Serif

Requirements
Must have
• Wordpress Implementation afterwards - Details according to attached Project Information Document

```html
<!DOCTYPE html>
<html lang="de">
<head>
<meta charset="utf-8">
<title>RP-Steuerberatung</title>
<link href="https://fonts.googleapis.com/css2?family=Montserrat:wght@700;800&family=Mulish:wght@400;600;700&display=swap" rel="stylesheet">
<style>
:root{
  --navy:#0f1f38;
  --footer:#1c2a42;
  --footer-dark:#141e30;
  --text:#222;
  --muted:#555;
  --grey-btn:#a9a9a9;
  --divider:#e4e4e4;
  --white:#fff;
}
*{margin:0;padding:0;box-sizing:border-box}
html,body{width:1200px;height:1030px;overflow:hidden;background:var(--white);font-family:"Mulish",sans-serif;color:var(--text)}
.site{position:relative;width:1200px;height:1030px}

.header{position:absolute;top:0;left:0;width:1200px;height:65px;display:flex;align-items:center}
.brand{position:absolute;left:162px;top:14px;display:flex;align-items:center;gap:10px}
.brand-mark{width:22px;height:22px;background:var(--navy)}
.brand-name{font-family:"Montserrat",sans-serif;font-weight:700;font-size:15px;color:var(--navy);letter-spacing:.3px}
.nav{position:absolute;top:24px;left:584px;display:flex;gap:29px;list-style:none}
.nav a{font-size:14px;color:#666;text-decoration:none;letter-spacing:.2px}
.nav a.active{color:var(--navy);font-weight:700}

.hero{position:absolute;top:65px;left:0;width:1200px;height:472px;background:radial-gradient(ellipse at 60% 30%,#fbfbfb 0%,#f2f2f2 55%,#e9e9e9 100%);text-align:center}
.hero-title{position:absolute;top:154px;width:100%;font-family:"Montserrat",sans-serif;font-weight:800;font-size:34px;color:var(--navy)}
.hero-sub{position:absolute;top:205px;width:100%;font-weight:700;font-size:18px;line-height:27px;color:#333}
.hero-btn{position:absolute;top:275px;left:487px;width:226px;height:37px;background:var(--grey-btn);color:var(--white);font-size:14px;line-height:37px;clip-path:polygon(0 0,96% 0,100% 22%,100% 100%,4% 100%,0 78%)}

.features{position:absolute;top:598px;left:162px;width:876px;display:flex}
.feature{font-size:17px;line-height:23px;text-align:center;padding:0 12px}
.feature:nth-child(1){width:305px}
.feature:nth-child(2){width:262px;border-left:1px solid var(--divider);border-right:1px solid var(--divider)}
.feature:nth-child(3){width:309px}

.footer{position:absolute;top:730px;left:0;width:1200px;height:243px;background:var(--footer);color:var(--white)}
.footer-nav{position:absolute;top:64px;left:311px;width:578px;display:flex;justify-content:space-between;list-style:none}
.footer-nav a{color:var(--white);font-size:13.5px;text-decoration:none}
.footer-nav a.active{font-weight:700}
.footer-rule{position:absolute;top:104px;left:311px;width:578px;border-top:1px dashed #35445e}
.contact{position:absolute;top:135px;font-size:13.5px;line-height:18px}
.contact-phone{left:250px;width:126px;text-align:right}
.contact-mail{left:794px}
.icon{position:absolute;top:136px}
.footer-brand{position:absolute;top:140px;left:459px;display:flex;align-items:center;gap:12px}
.footer-brand .brand-mark{width:28px;height:28px;background:var(--white)}
.footer-brand .brand-name{color:var(--white);font-size:18px}

.copyright{position:absolute;top:973px;left:0;width:1200px;height:57px;background:var(--footer-dark);color:#e6e6e6;font-size:13.5px;line-height:57px;text-align:center}
</style>
</head>
<body>
<div class="site">
  <header class="header">
    <div class="brand"><span class="brand-mark"></span><span class="brand-name">RP STEUERBERATUNG</span></div>
    <ul class="nav">
      <li><a class="active" href="#">HEIM</a></li>
      <li><a href="#">LEISTUNGEN</a></li>
      <li><a href="#">ÜBER MICH</a></li>
      <li><a href="#">KONTAKT</a></li>
      <li><a href="#">IMPRESSUM</a></li>
    </ul>
  </header>

  <section class="hero" role="img" aria-label="Heller Hintergrund mit fließender Punktwelle">
    <h1 class="hero-title">Willkommen bei RP-Steuerberatung!</h1>
    <p class="hero-sub">Ihrem Spezialisten bei allen steuerlichen Themen rund um<br>Einkünfte &amp; Vermögen aus Krypto-Assets.</p>
    <a class="hero-btn">Weiter zu unseren Leistungen</a>
  </section>

  <section class="features">
    <p class="feature">Dann mach ich eine Schweizer Holding-Gesellschaft– dort zahlt man fast keine Steuern</p>
    <p class="feature">Dann melde ich einfach meinen Hauptwohnsitz in Österreich ab</p>
    <p class="feature">Dann lass ich meine Kryptos auf einer Börse in Singapur, dort ist das steuerfrei</p>
  </section>

  <footer class="footer">
    <ul class="footer-nav">
      <li><a class="active" href="#">Heim</a></li>
      <li><a href="#">Leistungen</a></li>
      <li><a href="#">Über mich</a></li>
      <li><a href="#">Kontakt</a></li>
      <li><a href="#">Impressum</a></li>
    </ul>
    <div class="footer-rule"></div>

    <div class="contact contact-phone">Telefon<br>+43 512 000 417</div>
    <svg class="icon" style="left:387px" width="36" height="36" viewBox="0 0 36 36" fill="none" stroke="#fff" stroke-width="1.4" stroke-linecap="round">
      <path d="M8 4c-2 1-4 3-4 6 0 9 11 22 22 22 3 0 5-2 6-4l-5-5-4 3c-4-2-8-6-10-10l3-4z"/>
      <path d="M20 6c5 1 9 5 10 10"/><path d="M20 11c3 1 4 3 5 5"/><path d="M21 1c7 1 13 7 14 14"/>
    </svg>

    <div class="footer-brand"><span class="brand-mark"></span><span class="brand-name">RP STEUERBERATUNG</span></div>

    <svg class="icon" style="left:753px" width="32" height="36" viewBox="0 0 32 36" fill="none" stroke="#fff" stroke-width="1.4" stroke-linejoin="round">
      <path d="M1 14l15-11 15 11v20H1z"/><path d="M1 14l15 11 15-11"/><path d="M1 34l11-10M31 34L20 24"/>
      <path d="M7 19V6h18v13"/><path d="M11 10h10M11 14h10"/>
    </svg>
    <div class="contact contact-mail">Email<br>office@rp-steuer.example</div>
  </footer>

  <div class="copyright">Copyright © 2022 RP STEUERBERATUNG. All Rights Reserved.</div>
</div>
</body>
</html>
```